Estate Agent/Real Estate valuation tool

We need a design for our our new estate agent valuation tool.

The tool allows users to book a valuation of their house/property with the estate agent, after they choose there property they can then complete their details and choose a booking time.

The mock up of the design we want is attached to this project.(Main Screen)

This also needs to be responsive so the design is easy to use on a mobile device.

Target Market(s)

estate agents

Industry/Entity Type

Real Estate Agent

Number of Pages Required

1 page

Requirements
Must have
• Section 2 and 3 greyed out when user is on step 1
• Section 1 and 3 greyed out when user is on step 2
• Section 1 and 2 greyed out when the user is on step 3
• *** Design must be shown for mobile/ipad and desktop
Nice to have
• Clean and Simple
Should not have
• Dark colours

```html
<!DOCTYPE html>
<html lang="en">
<head>
<meta charset="utf-8">
<title>Real Estate Valuation – Book Your Valuation Online</title>
<link rel="stylesheet" href="https://fonts.googleapis.com/css2?family=Noto+Serif:wght@400;700&family=Open+Sans:wght@400;600;700;800&display=swap">
<style>
  :root {
    --page-bg: #e9e9e7;
    --screen-bg: #ffffff;
    --ink: #1d1d1d;
    --muted: #6b6b6b;
    --orange: #f39a12;
    --orange-dark: #d9820a;
    --band-grey: #e4e4e4;
    --panel-grey: #f1f1f1;
    --field-border: #d6d6d6;
    --green: #3daa4a;
    --green-dark: #2f9040;
    --tab-black: #1b1b1b;
  }
  * { box-sizing: border-box; margin: 0; padding: 0; }
  html, body {
    width: 1200px; height: 799px; overflow: hidden;
    background: var(--page-bg);
  }
  body {
    display: flex; justify-content: center; align-items: center;
    font-family: "Open Sans", Arial, sans-serif;
    color: var(--ink);
  }
  .booking-screen {
    width: 470px; height: 760px;
    background: var(--screen-bg);
    box-shadow: 0 6px 24px rgba(0,0,0,.12);
    display: flex; flex-direction: column;
    overflow: hidden;
  }
  .brand {
    display: flex; flex-direction: column; align-items: center;
    padding: 26px 0 20px;
  }
  .brand-mark {
    width: 40px; height: 40px; border-radius: 50%;
    background: var(--orange-dark);
    margin-bottom: 10px;
  }
  .brand-name {
    font-family: "Noto Serif", Georgia, serif;
    font-weight: 700; font-size: 28px; letter-spacing: -.2px;
  }
  .promo-band {
    background: var(--band-grey);
    text-align: center;
    padding: 17px 0;
    font-weight: 800; font-size: 18px;
    color: var(--orange);
    text-transform: uppercase;
  }
  .step { margin: 16px 14px 0; }
  .step-tab {
    display: inline-flex; align-items: center; gap: 10px;
    height: 48px; padding: 0 44px 0 8px;
    background: var(--tab-black);
    color: #fff;
    clip-path: polygon(0 0, calc(100% - 24px) 0, 100% 50%, calc(100% - 24px) 100%, 0 100%);
  }
  .step-number {
    width: 34px; height: 34px; border-radius: 50%;
    background: var(--orange);
    color: var(--tab-black);
    font-weight: 700; font-size: 16px;
    display: flex; align-items: center; justify-content: center;
  }
  .step-title {
    font-family: "Noto Serif", Georgia, serif;
    font-weight: 400; font-size: 24px;
  }
  .step-body {
    background: var(--panel-grey);
    border: 1px solid #e2e2e2;
    padding: 16px 16px 14px;
    margin-top: -4px;
    display: flex; flex-direction: column; gap: 10px;
  }
  .field {
    display: flex; height: 44px;
    background: #fff;
    border: 1px solid var(--field-border);
    align-items: center;
  }
  .field-value {
    flex: 1; padding: 0 14px;
    font-size: 15px; color: var(--muted);
  }
  .search-button {
    width: 44px; height: 44px; margin: -1px -1px -1px 0;
    background: var(--green);
    display: flex; align-items: center; justify-content: center;
  }
  .proceed-button {
    height: 46px; margin-top: 6px;
    background: var(--green);
    border-bottom: 3px solid var(--green-dark);
    color: #fff;
    font-family: "Noto Serif", Georgia, serif;
    font-weight: 700; font-size: 17px; letter-spacing: .5px;
    display: flex; align-items: center; justify-content: center;
    text-transform: uppercase;
  }
  .step--collapsed {
    margin: 16px 0 0;
    background: var(--tab-black);
    height: 50px;
  }
  .step--collapsed + .step--collapsed { margin-top: 10px; }
  .step--collapsed .step-tab {
    height: 50px; padding-left: 14px;
    background: var(--orange);
  }
  .step--collapsed .step-number {
    background: var(--orange-dark); color: #fff;
    border: 2px solid #f7c06a;
  }
  .step--inactive { opacity: .55; }
</style>
</head>
<body>
  <main class="booking-screen">
    <header class="brand">
      <span class="brand-mark"></span>
      <h1 class="brand-name">Real Estate Valuation</h1>
    </header>

    <div class="promo-band">Book your valuation online</div>

    <section class="step step--active">
      <div class="step-tab">
        <span class="step-number">01</span>
        <h2 class="step-title">Property Details</h2>
      </div>
      <div class="step-body">
        <div class="field"><span class="field-value">125648</span></div>
        <div class="field">
          <span class="field-value">123 Test Street</span>
          <span class="search-button">
            <svg width="20" height="20" viewBox="0 0 24 24" fill="none" stroke="#fff" stroke-width="2.6" stroke-linecap="round">
              <circle cx="10" cy="10" r="6.5"/>
              <line x1="15" y1="15" x2="21" y2="21"/>
            </svg>
          </span>
        </div>
        <div class="field"><span class="field-value">Test City</span></div>
        <div class="field"><span class="field-value">Test Country</span></div>
        <div class="proceed-button">Proceed</div>
      </div>
    </section>

    <section class="step step--collapsed step--inactive">
      <div class="step-tab">
        <span class="step-number">02</span>
        <h2 class="step-title">Your Details</h2>
      </div>
    </section>

    <section class="step step--collapsed step--inactive">
      <div class="step-tab">
        <span class="step-number">03</span>
        <h2 class="step-title">Booking Time</h2>
      </div>
    </section>
  </main>
</body>
</html>
```